Cutting Edge Energy Company PowerPoint Design

Need PowerPoint template for energy company whose primary focus is to extract oil and gas from subsurface reservoirs. Would like design to have a sleek, modern, cutting edge feel. Template will be used to present to Investors. Need to have a PR/Investor relations feel with the ability to present data, economics, graphs, and photos. Needs to incorporate company logo and company stock photos where possible. Design needs to be able to interchange company names Talvane Resources & Brackmoor Resources within the template depending on audience. Company colors can be seen in Logo. Source files can be provided.

```html
<!DOCTYPE html>
<html lang="en">
<head>
<meta charset="utf-8">
<title>Talvane Resources – Investor Presentation Template</title>
<link rel="stylesheet" href="https://fonts.googleapis.com/css2?family=Michroma&family=Roboto:ital,wght@0,400;0,700;1,400&display=swap">
<style>
:root{
  --blue:#0b4a86;
  --ink:#0c0c0e;
  --white:#ffffff;
  --grey:#5b5b5b;
  --muted:#a9a9a9;
  --faint:#e2e2e2;
  --page:#ffffff;
}
*{box-sizing:border-box;margin:0;padding:0}
html,body{width:1200px;height:2194px;overflow:hidden;background:var(--page)}
body{position:relative;font-family:"Roboto",Arial,sans-serif;color:var(--grey)}
.slide{position:absolute;width:534px;height:300px;background:var(--white);overflow:hidden;box-shadow:0 10px 26px rgba(0,0,0,.28)}
.abs{position:absolute}
.display{font-family:"Michroma",Arial,sans-serif;text-transform:uppercase;line-height:1.05;color:var(--ink)}
.display .hl{color:var(--blue)}
.on-dark{color:var(--white)}
.brand{position:absolute;display:flex;align-items:center;gap:4px;font-family:"Michroma",Arial,sans-serif;font-size:6px;text-transform:uppercase;color:var(--blue);white-space:nowrap}
.brand::before{content:"";width:7px;height:7px;background:currentColor}
.brand.light{color:var(--white)}
.brand.lg{font-size:13px;gap:8px}
.brand.lg::before{width:14px;height:14px}
.footer-url{position:absolute;right:40px;bottom:9px;font-size:5px;color:var(--muted)}
.page-no{position:absolute;right:14px;bottom:5px;width:20px;height:14px;background:var(--blue);color:var(--white);font-family:"Michroma",Arial,sans-serif;font-size:5px;display:flex;align-items:center;justify-content:center}
.photo{position:absolute}
.sunset{background:linear-gradient(165deg,#2b0703 0%,#a3240a 30%,#e5530f 55%,#f5a21c 72%,#2a0a03 88%)}
.mono{background:linear-gradient(180deg,#3e3e3e 0%,#8a8a8a 50%,#6b6b6b 62%,#232323 100%)}
.aerial{background:linear-gradient(155deg,#3f3226 0%,#6e5a46 40%,#a8967c 62%,#5e4b39 100%)}
.skyrig{background:linear-gradient(180deg,#1b5aa3 0%,#7ea6cf 42%,#8a6d50 58%,#5a4230 100%)}
.body{font-size:5.6px;line-height:1.55;color:var(--grey);text-align:justify}
.bullets{list-style:none}
.bullets li{position:relative;padding-left:8px;margin-bottom:4px}
.bullets li::before{content:"";position:absolute;left:0;top:2px;width:3px;height:3px;background:currentColor}
.sub-head{font-weight:700;color:var(--blue);text-transform:uppercase}
</style>
</head>
<body>

<!-- 1 Title -->
<section class="slide" style="left:51px;top:104px">
  <div class="abs" style="left:0;top:59px;width:534px;height:181px;background:var(--ink)"></div>
  <div class="photo sunset" role="img" aria-label="Pumpjack silhouette against an orange sunset" style="left:0;top:0;width:240px;height:300px;clip-path:polygon(0 0,100% 50%,0 100%)"></div>
  <div class="brand lg" style="left:282px;top:85px">Talvane Resources</div>
  <h1 class="display hl" style="position:absolute;left:285px;top:124px;font-size:15px;font-weight:400;color:var(--blue)">Place here your<br>presentation title</h1>
  <p class="abs" style="left:304px;top:178px;font-size:9px;color:var(--blue)">Place Here your sub title presentation</p>
  <p class="abs" style="left:356px;top:205px;font-size:5.5px;color:var(--blue);text-align:center;line-height:1.5"><b>Presenter:</b> Alex Marlow<br><b>Date :</b> Jan 15, 2022</p>
  <p class="abs" style="left:225px;top:285px;font-size:6px;color:var(--blue)">www.talvaneresources.com/</p>
</section>

<!-- 2 Table of contents -->
<section class="slide" style="left:608px;top:104px">
  <div class="photo mono" role="img" aria-label="Black and white pumpjack in an oil field" style="left:0;top:0;width:253px;height:300px"></div>
  <div class="brand light" style="left:26px;top:30px">Talvane Resources</div>
  <h2 class="display on-dark" style="position:absolute;left:0;width:253px;top:194px;text-align:center;font-size:24px;font-weight:400">Table of<br>contents</h2>
  <div class="brand" style="right:24px;top:30px">Talvane Resources</div>
  <ol class="abs" style="left:268px;top:54px;list-style:none">
    <li style="display:flex;gap:10px;height:36.5px"><span style="font:italic 20px Roboto,sans-serif;color:var(--blue)">01</span><span><b class="display" style="font-size:9px;font-weight:400;color:var(--blue)">Introduction</b><br><span style="font-size:5px;color:var(--muted)">Lorem Ipsum is simply dummy text of the printing</span></span></li>
    <li style="display:flex;gap:10px;height:36.5px"><span style="font:italic 20px Roboto,sans-serif;color:var(--blue)">02</span><span><b class="display" style="font-size:9px;font-weight:400;color:var(--blue)">About us</b><br><span style="font-size:5px;color:var(--muted)">Lorem Ipsum is simply dummy text of the printing</span></span></li>
    <li style="display:flex;gap:10px;height:36.5px"><span style="font:italic 20px Roboto,sans-serif;color:var(--blue)">03</span><span><b class="display" style="font-size:9px;font-weight:400;color:var(--blue)">What we do</b><br><span style="font-size:5px;color:var(--muted)">Lorem Ipsum is simply dummy text of the printing</span></span></li>
    <li style="display:flex;gap:10px;height:36.5px"><span style="font:italic 20px Roboto,sans-serif;color:var(--blue)">04</span><span><b class="display" style="font-size:9px;font-weight:400;color:var(--blue)">Our proposal</b><br><span style="font-size:5px;color:var(--muted)">Lorem Ipsum is simply dummy text of the printing</span></span></li>
    <li style="display:flex;gap:10px;height:36.5px"><span style="font:italic 20px Roboto,sans-serif;color:var(--blue)">05</span><span><b class="display" style="font-size:9px;font-weight:400;color:var(--blue)">Analysis</b><br><span style="font-size:5px;color:var(--muted)">Lorem Ipsum is simply dummy text of the printing</span></span></li>
    <li style="display:flex;gap:10px;height:36.5px"><span style="font:italic 20px Roboto,sans-serif;color:var(--blue)">06</span><span><b class="display" style="font-size:9px;font-weight:400;color:var(--blue)">Contact us</b><br><span style="font-size:5px;color:var(--muted)">Lorem Ipsum is simply dummy text of the printing</span></span></li>
  </ol>
  <p class="footer-url">www.talvaneresources.com/</p><span class="page-no">2</span>
</section>

<!-- 3 Introduction -->
<section class="slide" style="left:51px;top:439px">
  <div class="photo mono" role="img" aria-label="Black and white oil field with drilling rig and pumpjack" style="left:0;top:0;width:534px;height:300px"></div>
  <div class="brand lg light" style="left:67px;top:42px">Talvane Resources</div>
  <div class="abs" style="left:0;top:230px;width:325px;height:60px;background:var(--blue)"></div>
  <h2 class="display on-dark" style="position:absolute;left:67px;top:246px;font-size:24px;font-weight:400">Introduction</h2>
</section>

<!-- 4 About -->
<section class="slide" style="left:608px;top:439px">
  <div class="photo aerial" role="img" aria-label="Aerial view of a drilling rig site" style="left:14px;top:14px;width:238px;height:273px"></div>
  <div class="brand" style="right:24px;top:30px">Talvane Resources</div>
  <h2 class="display" style="position:absolute;left:268px;top:136px;font-size:24px;font-weight:400">About our<br><span class="hl" style="margin-left:14px">company</span></h2>
  <p class="abs body" style="left:264px;top:199px;width:246px;font-size:7px">Lorem Ipsum is simply dummy text of the printing and typesetting industry. Lorem Ipsum has been the industry's standard dummy text ever since the 1500s, when an unknown printer took a galley of type and scrambled it to make a type specimen book.</p>
  <p class="footer-url">www.talvaneresources.com/</p><span class="page-no">6</span>
</section>

<!-- 5 Vision -->
<section class="slide" style="left:51px;top:774px">
  <div class="abs" style="left:0;top:102px;width:534px;height:150px;background:var(--blue)"></div>
  <div class="photo skyrig" role="img" aria-label="Drilling rig under a blue sky" style="left:88px;top:0;width:220px;height:300px"></div>
  <h2 class="display" style="position:absolute;left:20px;top:20px;font-size:24px;font-weight:400">Our<br><span class="hl">vision</span></h2>
  <div class="brand" style="left:318px;top:72px;font-size:11px;gap:7px">Talvane Resources</div>
  <p class="abs" style="left:321px;top:108px;font-size:10px;font-weight:700;color:var(--white)">energy company</p>
  <ul class="abs bullets body" style="left:322px;top:126px;width:200px;color:var(--white);font-size:5.4px">
    <li>Lorem Ipsum is simply dummy text of the printing and typesetting industry.</li>
    <li>Lorem Ipsum has been the industry's standard dummy text ever since the 1500s, when an unknown printer took a galley of type and scrambled it to make a type specimen book.</li>
    <li>It has survived not only five centuries, but also the leap into electronic typesetting, remaining essentially unchanged. It was popularized in the 1960s with the release of Letraset sheets containing</li>
    <li>Lorem Ipsum passages, and more recently with desktop publishing software like Aldus PageMaker including versions</li>
  </ul>
  <p class="footer-url">www.talvaneresources.com/</p><span class="page-no">5</span>
</section>

<!-- 6 Mission -->
<section class="slide" style="left:608px;top:774px">
  <div class="abs" style="left:0;top:68px;width:534px;height:90px;background:var(--ink)"></div>
  <div class="photo skyrig" role="img" aria-label="Drilling rig and site equipment under a blue sky" style="left:23px;top:0;width:207px;height:266px"></div>
  <div class="brand" style="right:24px;top:30px">Talvane Resources</div>
  <h2 class="display on-dark" style="position:absolute;left:250px;top:88px;font-size:24px;font-weight:400">Our <span class="hl">mission</span></h2>
  <p class="abs" style="left:252px;top:125px;font-size:10px;color:#cfcfcf">energy company</p>
  <ul class="abs bullets body" style="left:250px;top:170px;width:260px;color:#333;font-size:5.6px">
    <li>Lorem Ipsum is simply dummy text of the printing and typesetting industry. Lorem Ipsum has been the industry's standard dummy text ever since the 1500s, when an unknown printer took a galley of type and scrambled it to make a type specimen book.</li>
    <li>It has survived not only five centuries, but also the leap into electronic typesetting, remaining essentially unchanged. It was popularized in the 1960s with the release of Letraset sheets containing Lorem Ipsum passages, and more recently with desktop publishing software like Aldus PageMaker including versions of Lorem Ipsum.</li>
  </ul>
  <p class="footer-url">www.talvaneresources.com/</p><span class="page-no">4</span>
</section>

<!-- 7 Title slide layout -->
<section class="slide" style="left:51px;top:1108px">
  <div class="photo aerial" role="img" aria-label="Aerial view of a drilling rig site" style="left:0;top:0;width:267px;height:300px"></div>
  <div class="brand" style="right:24px;top:30px">Talvane Resources</div>
  <div class="abs" style="left:200px;top:47px;width:334px;height:82px;background:var(--ink)"></div>
  <h2 class="display on-dark" style="position:absolute;left:217px;top:62px;font-size:24px;font-weight:400">Your title<br><span class="hl">slide goes here</span></h2>
  <div class="abs" style="left:277px;top:150px;width:235px">
    <p class="sub-head" style="font-size:9px">Lorem ipsum is dummy text</p>
    <p class="body" style="text-align:left;margin:3px 0 11px">Lorem Ipsum is simply dummy text of the printing and typesetting industry. Lorem Ipsum has been the industry's standard dummy text ever since the 1500s, when an unknown printer took a galley of type and scrambled it to make a type specimen book.</p>
    <p class="sub-head" style="font-size:9px">Lorem ipsum is dummy text</p>
    <p class="body" style="text-align:left;margin-top:3px">Lorem Ipsum is simply dummy text of the printing and typesetting industry. Lorem Ipsum has been the industry's standard dummy text ever since the 1500s, when an unknown printer took a galley of type and scrambled it to make a type specimen book.</p>
  </div>
  <p class="footer-url">www.talvaneresources.com/</p><span class="page-no">7</span>
</section>

<!-- 8 Services -->
<section class="slide" style="left:608px;top:1108px">
  <div class="brand" style="left:26px;top:30px">Talvane Resources</div>
  <div class="photo mono" role="img" aria-label="Black and white pumpjack and drilling rig" style="left:26px;top:48px;width:258px;height:127px"></div>
  <div class="abs" style="left:26px;top:178px;width:258px;height:80px;background:var(--ink)"></div>
  <h2 class="display on-dark" style="position:absolute;left:26px;width:258px;top:196px;text-align:center;font-size:24px;font-weight:400">Our<br><span class="hl">services</span></h2>
  <div class="abs" style="left:305px;top:50px;width:212px">
    <p class="sub-head" style="font-size:9.5px">Lorem ipsum is dummy text</p>
    <p class="body" style="margin:3px 0 14px">Lorem Ipsum is simply dummy text of the printing and typesetting industry. Lorem Ipsum has been the industry's standard dummy text ever since the 1500s, when an unknown printer took a galley of type and scrambled it to make a type</p>
    <p class="sub-head" style="font-size:9.5px">Lorem ipsum is dummy text</p>
    <p class="body" style="margin:3px 0 14px">Lorem Ipsum is simply dummy text of the printing and typesetting industry. Lorem Ipsum has been the industry's standard dummy text ever since the 1500s, when an unknown printer took a galley of type and scrambled it to make a type</p>
    <p class="sub-head" style="font-size:9.5px">Lorem ipsum is dummy text</p>
    <p class="body" style="margin-top:3px">Lorem Ipsum is simply dummy text of the printing and typesetting industry. Lorem Ipsum has been the industry's standard dummy text ever since the 1500s, when an unknown printer took a galley of type and scrambled it to make a type</p>
  </div>
  <p class="footer-url">www.talvaneresources.com/</p><span class="page-no">8</span>
</section>

<!-- 9 Latest project -->
<section class="slide" style="left:51px;top:1443px;background:var(--ink)">
  <div class="photo skyrig" role="img" aria-label="Drilling rig on open land under a blue sky" style="left:221px;top:14px;width:300px;height:271px"></div>
  <div class="brand light" style="left:26px;top:30px">Talvane Resources</div>
  <h2 class="display on-dark" style="position:absolute;left:20px;top:58px;font-size:23px;font-weight:400">Our latest<br><span class="hl">project</span></h2>
  <p class="abs body" style="left:20px;top:115px;width:194px;color:var(--white);text-transform:uppercase;font-size:5.8px;line-height:1.4">Lorem Ipsum is simply dummy text of the printing and typesetting industry. Lorem Ipsum has been the industry's standard dummy text ever since the 1500s, when an unknown printer took a galley of type and scrambled it to make a type specimen book.</p>
  <ul class="abs bullets body" style="left:20px;top:178px;width:194px;color:var(--white);font-size:5.2px">
    <li>Lorem Ipsum is simply dummy text of the printing and typesetting industry.</li>
    <li>Lorem Ipsum has been the industry's standard dummy text ever since the 1500s, when an unknown printer took a galley of type and scrambled it to make a type specimen book.</li>
    <li>It has survived not only five centuries, but also the leap into electronic typesetting, remaining essentially unchanged.</li>
    <li>It was popularized in the 1960s with the release of Letraset sheets containing Lorem Ipsum passages, and more recently with desktop</li>
  </ul>
</section>

<!-- 10 Latest projects -->
<section class="slide" style="left:608px;top:1443px">
  <h2 class="display" style="position:absolute;left:26px;top:31px;font-size:18px;font-weight:400">Our latest <span class="hl">projects</span></h2>
  <div class="brand" style="right:24px;top:36px">Talvane Resources</div>
  <div class="photo skyrig" role="img" aria-label="Drilling rig site under a blue sky" style="left:43px;top:73px;width:209px;height:106px"></div>
  <div class="photo aerial" role="img" aria-label="Aerial view of a drilling rig site" style="left:280px;top:73px;width:209px;height:106px"></div>
  <div class="abs display on-dark" style="left:62px;top:170px;width:171px;height:20px;background:var(--blue);display:flex;align-items:center;justify-content:center;font-size:10px">Project 1</div>
  <div class="abs display on-dark" style="left:299px;top:170px;width:171px;height:20px;background:var(--ink);display:flex;align-items:center;justify-content:center;font-size:10px">Project 2</div>
  <ul class="abs bullets body" style="left:46px;top:202px;width:206px;font-size:5.2px;line-height:1.45">
    <li>Lorem Ipsum is simply dummy text of the printing and typesetting industry. Lorem Ipsum has been the industry's standard dummy text ever since the 1500s, when an unknown printer took a galley of type and scrambled it to make a type specimen book.</li>
    <li>Lorem Ipsum is simply dummy text of the printing and typesetting industry. Lorem Ipsum has been the industry's standard dummy text ever since the 1500s, when an unknown printer took a galley of type and scrambled it to make a type specimen book.</li>
  </ul>
  <ul class="abs bullets body" style="left:283px;top:202px;width:206px;font-size:5.2px;line-height:1.45">
    <li>Lorem Ipsum is simply dummy text of the printing and typesetting industry. Lorem Ipsum has been the industry's standard dummy text ever since the 1500s, when an unknown printer took a galley of type and scrambled it to make a type specimen book.</li>
    <li>Lorem Ipsum is simply dummy text of the printing and typesetting industry. Lorem Ipsum has been the industry's standard dummy text ever since the 1500s, when an unknown printer took a galley of type and scrambled it to make a type specimen book.</li>
  </ul>
  <p class="footer-url">www.talvaneresources.com/</p><span class="page-no">10</span>
</section>

<!-- 11 Statement -->
<section class="slide" style="left:51px;top:1777px">
  <div class="brand" style="right:24px;top:30px">Talvane Resources</div>
  <div class="photo mono" role="img" aria-label="Black and white oil field with pumpjack" style="left:0;top:51px;width:534px;height:198px"></div>
  <p class="display on-dark" style="position:absolute;left:64px;top:84px;font-size:17.5px;line-height:1.4">Lorem ipsum is<br>simply dummy<br>text of the<br>printing and<br>typesetting<br>industry.</p>
  <p class="footer-url">www.talvaneresources.com/</p><span class="page-no">11</span>
</section>

<!-- 12 SWOT -->
<section class="slide" style="left:608px;top:1777px">
  <div class="abs" style="left:267px;top:0;width:1px;height:300px;background:#cfcfcf"></div>
  <span class="abs" style="left:200px;top:18px;font:italic 62px Roboto,sans-serif;color:var(--faint)">S</span>
  <span class="abs" style="left:308px;top:18px;font:italic 62px Roboto,sans-serif;color:var(--faint)">W</span>
  <span class="abs" style="left:198px;top:170px;font:italic 62px Roboto,sans-serif;color:var(--faint)">O</span>
  <span class="abs" style="left:308px;top:170px;font:italic 62px Roboto,sans-serif;color:var(--faint)">T</span>
  <div class="brand" style="right:24px;top:33px">Talvane Resources</div>
  <div class="abs" style="left:22px;top:74px;width:225px;text-align:right">
    <p class="display hl" style="font-size:10px;color:var(--blue)">Strengths</p>
    <p class="body" style="text-align:right;margin-top:3px;font-size:5.3px;line-height:1.5">Lorem Ipsum is simply dummy text of the printing and typesetting industry. Lorem Ipsum has been the industry's standard dummy text ever since the 1500s, when an unknown printer took a galley of type and scrambled it to make a type</p>
  </div>
  <div class="abs" style="left:310px;top:74px;width:185px">
    <p class="display" style="font-size:10px;color:var(--blue)">Weaknesses</p>
    <p class="body" style="text-align:left;margin-top:3px;font-size:5.3px;line-height:1.5">Lorem Ipsum is simply dummy text of the printing and typesetting industry. Lorem Ipsum has been the industry's standard dummy text ever since the 1500s, when an unknown printer took a galley of type and scrambled it to make a type</p>
  </div>
  <div class="abs" style="left:22px;top:131px;width:490px;height:40px;background:var(--ink)"></div>
  <h2 class="display on-dark" style="position:absolute;left:22px;width:490px;top:143px;text-align:center;font-size:22px;font-weight:400">Swot <span class="hl">analysis</span></h2>
  <div class="abs" style="left:22px;top:227px;width:225px;text-align:right">
    <p class="display" style="font-size:10px;color:var(--blue)">Opportunities</p>
    <p class="body" style="text-align:right;margin-top:3px;font-size:5.3px;line-height:1.5">Lorem Ipsum is simply dummy text of the printing and typesetting industry. Lorem Ipsum has been the industry's standard dummy text ever since the 1500s, when an unknown printer took a galley of type and scrambled it to make a type</p>
  </div>
  <div class="abs" style="left:310px;top:227px;width:185px">
    <p class="display" style="font-size:10px;color:var(--blue)">Threats</p>
    <p class="body" style="text-align:left;margin-top:3px;font-size:5.3px;line-height:1.5">Lorem Ipsum is simply dummy text of the printing and typesetting industry. Lorem Ipsum has been the industry's standard dummy text ever since the 1500s, when an unknown printer took a galley of type and scrambled it to make a type</p>
  </div>
  <p class="footer-url">www.talvaneresources.com/</p><span class="page-no">12</span>
</section>

</body>
</html>
```